8"x5" postcard for Wireless Internet introduction to new mountain town market

I need to market high speed internet to a resort mountain town without doing the obvious laptop on a mountain top thing, so tired. We are going to be competing directly with another provider with same cost, but we will be offering free installation. The area is Aspen Colorado, so the clientele are outdoor types who have suffered for years from being disconnected in their mountain town. We offer fast internet and excellent customer service from people who live in their neck of the woods.

Target Market(s)

23-55 years old, both resort living, families and ski bums

Font styles to use
Sans Serif

Colors

Designer to choose colors to be used in the design.

Requirements
Must have
• Visual appeal and fresh verbiage. We don't mind being a little edgy. We are a young company and we want to appeal to people looking for a provider who gets them. We prefer a clean look.
Nice to have
• Nice to have colors that match our logo
Should not have
• stuffy concepts or verbiage that is too much like a car salesman. We don't want to look like a 'big box' company.

```html
<!DOCTYPE html>
<html lang="en">
<head>
<meta charset="utf-8">
<title>Ridgeway Broadband Postcard</title>
<link href="https://fonts.googleapis.com/css2?family=Montserrat:wght@300;700;800;900&family=Oswald:wght@600&family=Poppins:wght@600&display=swap" rel="stylesheet">
<style>
  :root {
    --bg: #8a8a8a;
    --white: #ffffff;
    --yellow: #f5dc1e;
    --yellow-deep: #e2c800;
    --orange: #fbb02d;
    --orange-light: #fdbf45;
    --ink: #111111;
    --text-dark: #1d1d1d;
    --photo-a: #d9e6ee;
    --photo-b: #a9bfd3;
    --photo-c: #c9a98a;
  }
  html, body {
    margin: 0;
    width: 1200px;
    height: 1200px;
    overflow: hidden;
    background: var(--bg);
  }
  .postcard {
    position: absolute;
    left: 50px;
    top: 295px;
    width: 1100px;
    height: 610px;
    background: var(--white);
    overflow: hidden;
    font-family: "Montserrat", sans-serif;
  }
  .top-stripe {
    position: absolute; left: 0; top: 0; width: 100%; height: 22px;
    background: var(--yellow);
  }
  .bottom-band {
    position: absolute; left: 0; bottom: 0; width: 100%; height: 30px;
    background: var(--ink);
  }
  .brand {
    position: absolute; left: 66px; top: 46px;
    display: flex; align-items: center; gap: 16px;
  }
  .brand-dot {
    width: 62px; height: 62px; border-radius: 50%;
    background: var(--orange);
  }
  .brand-name {
    font-weight: 800; font-size: 30px; letter-spacing: 1px;
    color: var(--text-dark); line-height: 1;
  }
  .photo {
    position: absolute; left: 0; top: 122px; width: 613px; height: 372px;
    background: linear-gradient(120deg, var(--photo-a) 0%, var(--photo-b) 55%, var(--photo-c) 100%);
  }
  .online-label {
    position: absolute; left: 30px; top: 505px;
    font-weight: 700; font-size: 30px; color: var(--yellow);
  }
  .online-url {
    position: absolute; left: 30px; top: 545px;
    display: flex; align-items: center; gap: 14px;
    font-weight: 700; font-size: 22px; color: var(--text-dark);
  }
  .online-url svg { width: 20px; height: 20px; }
  .offer-panel {
    position: absolute; left: 613px; top: 0; width: 410px; height: 610px;
    background: linear-gradient(180deg, var(--yellow) 0%, var(--yellow-deep) 100%);
  }
  .offer-panel .chevron {
    position: absolute; left: 0; top: 0; width: 410px; height: 460px;
  }
  .headline-top {
    position: absolute; left: 0; width: 410px; top: 28px; text-align: center;
    font-family: "Oswald", sans-serif; font-weight: 600; font-size: 78px;
    color: var(--white); line-height: 1; letter-spacing: 0.5px;
  }
  .headline-main {
    position: absolute; left: 0; width: 410px; top: 118px; text-align: center;
    font-weight: 900; font-size: 74px; color: var(--ink); line-height: 1;
  }
  .features {
    position: absolute; left: 20px; width: 370px; top: 214px;
    margin: 0; padding: 0; list-style: none; text-align: center;
    font-family: "Poppins", sans-serif; font-weight: 600; font-size: 21px;
    color: var(--text-dark);
  }
  .features li {
    height: 45px; line-height: 45px;
    background: linear-gradient(90deg, transparent, rgba(255,255,255,0.6), transparent) bottom / 100% 1px no-repeat;
  }
  .features li:last-child { background: none; }
  .cta-label {
    position: absolute; left: 0; width: 410px; top: 470px; text-align: center;
    font-weight: 300; font-size: 44px; color: var(--ink); letter-spacing: 1px;
  }
  .cta-phone {
    position: absolute; left: 0; width: 410px; top: 520px; text-align: center;
    font-weight: 800; font-size: 44px; color: var(--ink);
  }
</style>
</head>
<body>
  <div class="postcard">
    <div class="top-stripe"></div>
    <div class="bottom-band"></div>

    <div class="brand">
      <div class="brand-dot"></div>
      <div class="brand-name">RIDGEWAY BROADBAND</div>
    </div>

    <div class="photo" role="img" aria-label="Photo of a young couple sitting on a living room floor, excitedly looking at a laptop"></div>

    <div class="online-label">Or visit us online at</div>
    <div class="online-url">
      <svg viewBox="0 0 20 20" aria-hidden="true">
        <circle cx="10" cy="10" r="10" fill="var(--orange)"/>
        <path d="M8 5.5 L13 10 L8 14.5" fill="none" stroke="#fff" stroke-width="2.4"/>
      </svg>
      <span>www.ridgewaynet.com/go</span>
    </div>

    <div class="offer-panel">
      <svg class="chevron" viewBox="0 0 410 460" aria-hidden="true">
        <defs>
          <linearGradient id="orangeFade" x1="0" y1="0" x2="1" y2="1">
            <stop offset="0" stop-color="var(--orange)"/>
            <stop offset="1" stop-color="var(--orange-light)"/>
          </linearGradient>
        </defs>
        <polygon points="0,0 410,0 410,400 205,455 0,400" fill="url(#orangeFade)"/>
      </svg>
      <div class="headline-top">BETTER, NOT</div>
      <div class="headline-main">BIGGER!</div>
      <ul class="features">
        <li>Free residential Installation</li>
        <li>In-House Tech Support</li>
        <li>10, 25 and 40Mbps speeds</li>
        <li>Prices start at $59.95</li>
      </ul>
      <div class="cta-label">CALL NOW!</div>
      <div class="cta-phone">1 888 555 0142</div>
    </div>
  </div>
</body>
</html>
```